Press Upon Ink needs a New Website Design

Press Upon Ink is a small rubber stamp & scrapbook company operating in the arts & crafts space. We currently own 6 company brands plus Press Upon Ink which is the main business & website, www.pressuponink.net.
We are launching a new eCommerce store to bring all the companies under one shopping platform instead of the 6 there are currently. We need a new site design that incorporates the shop by brand idea making it super easy to navigate and understand. Brand logos should be displayed on all pages in header design similar to http://www.tidewove.com and https://bazaar.quellmark.com
The brand logo for Bravado! Stamps is currently being designed so that one is missing from the brief.
Top menu: Home, Shop, Videos, Gallery, Blogs, Show Schedule, PUI Brands or Brands
Utilize “Welcome to PressUponInk” tagline in design
Include “Art Rubber Stamps and Scrapbooking Supplies” tagline on at least home page
Need 3 pages designed, must be designed with responsive in mind.
Home page
Product Listing page
Product Detail page
Colors
Browns - use colors from background image attached
#981E1E
# 3B2313
Competitors
http://craftlostfree.com
https://inkersunnamed.com
http://www.morvelsllc.com
http://www.lubrofcraft.com
http://www.quvprints.com
http://www.thistlebrand.us
The shopping cart system being used is Cartwell (http://demo.cartwell.com/) if you are familiar with creating html templates for Cartwell there is additional opportunity to convert the design into html/css
Target Market(s)
Handmade Cardmakers, Scrapbookers, Papercrafters

```html
<!DOCTYPE html>
<html lang="en">
<head>
<meta charset="utf-8">
<title>Press Upon Ink – Art Rubber Stamps and Scrapbooking Supplies</title>
<link rel="stylesheet" href="https://fonts.googleapis.com/css2?family=Open+Sans:wght@400;600;700&family=Kaushan+Script&family=Great+Vibes&family=Archivo+Black&family=PT+Serif&display=swap">
<style>
:root{
  --red:#981e1e;
  --brown:#3b2313;
  --ink:#333;
  --muted:#666;
  --line:#dcdcdc;
  --yellow:#fdc11f;
  --white:#fff;
}
*{box-sizing:border-box;margin:0;padding:0}
html,body{width:699px;height:1200px;overflow:hidden}
body{position:relative;font-family:"Open Sans",sans-serif;color:var(--ink);
  background:linear-gradient(180deg,#f3e6f0 0%,#eef3e4 30%,#f0eef6 55%,#fbe9e1 80%,#f5d9d6 100%)}
.abs{position:absolute}
.page{position:absolute;left:42px;top:0;width:616px;height:1200px;background:var(--white)}
.brand-row{left:58px;top:14px;width:584px;height:32px;display:flex;justify-content:space-between;align-items:center}
.brand-name{font-size:11px;font-weight:600;color:#8a8a8a;letter-spacing:.5px}
.account{left:58px;top:108px;font-size:6.5px;letter-spacing:.6px;color:var(--muted)}
.account span{margin-right:10px}
.logo{display:flex;align-items:center;gap:5px}
.logo .dot{width:14px;height:14px;border-radius:50%;background:var(--brown);flex:none}
.logo .name{font-weight:700;color:var(--brown);white-space:nowrap}
.header-logo{left:286px;top:97px}
.header-logo .name{font-size:14px}
.call{left:438px;top:106px;font-size:6.5px;letter-spacing:.4px;color:var(--muted)}
.call b{color:var(--red);font-weight:600}
.cart{left:557px;top:102px;font-size:6px;letter-spacing:.4px;color:var(--muted);display:flex;align-items:center;gap:6px}
.rule{height:1px;background:var(--line)}
.nav{left:58px;top:158px;width:584px;display:flex;justify-content:space-between;padding:0 11px 0 11px;font-size:7.5px;font-weight:700;letter-spacing:.8px;color:#444}
.hero{left:58px;top:186px;width:584px;height:278px;background:var(--yellow);overflow:hidden}
.hero-art{position:absolute;left:0;top:0;width:330px;height:278px;background:radial-gradient(circle at 45% 50%,#fed45a 0%,#fdc11f 70%)}
.offer{position:absolute;left:120px;top:70px;font-family:"Great Vibes",cursive;font-size:26px;color:var(--white)}
.sale{position:absolute;left:118px;top:98px;font-family:"Archivo Black",sans-serif;font-size:39px;line-height:38px;color:#111}
.badge{position:absolute;left:170px;top:192px;width:42px;height:42px;border-radius:50%;background:var(--white);display:flex;align-items:center;justify-content:center;font-weight:700;font-size:14px;color:#111}
.badge small{font-size:6px}
.welcome{position:absolute;left:366px;top:72px;font-family:"Kaushan Script",cursive;color:var(--brown);font-size:25px;line-height:30px}
.welcome .brandline{color:var(--red);font-size:24px}
.tagline{position:absolute;left:368px;top:134px;font-size:11.5px;line-height:17px;color:#222}
.btn{background:var(--red);color:var(--white);font-size:7px;letter-spacing:.6px;display:flex;align-items:center;justify-content:center}
.hero .btn{position:absolute;left:370px;top:184px;width:112px;height:24px;font-size:7.5px}
.arrows{position:absolute;left:548px;top:259px;display:flex;gap:2px}
.arrows div{width:14px;height:14px;background:var(--red)}
.search-label{left:58px;top:484px;font-size:7px;color:#444}
.field{height:18px;border:1px solid var(--line);font-size:5.5px;color:#aaa;letter-spacing:.4px;display:flex;align-items:center;justify-content:space-between;padding:0 7px}
.featured{left:58px;top:523px;font-size:8px;color:#444}
.featured small{font-size:5.5px;letter-spacing:.4px;margin-left:3px;color:#555}
.card{width:136px;height:183px;border:1px solid var(--line)}
.card .shot{position:absolute;left:24px;top:12px;width:86px;height:98px}
.card .title{position:absolute;left:0;top:120px;width:100%;text-align:center;font-size:7.5px;line-height:11.5px;letter-spacing:.5px;color:#444}
.card .price{position:absolute;left:15px;top:152px;font-family:"PT Serif",serif;font-size:12px;color:#333}
.card .btn{position:absolute;left:64px;top:151px;width:55px;height:16px;font-size:5.5px}
.news-label{left:60px;top:982px;font-size:7.5px;color:#444}
.social{left:530px;top:976px;display:flex;gap:3px}
.social div{width:19px;height:19px;border-radius:50%}
.foot-col{top:1028px;font-size:6px;letter-spacing:.4px;color:#555;line-height:12px}
.foot-col h4{font-size:8.5px;font-weight:400;letter-spacing:.3px;color:#333;margin-bottom:5px}
.footer-logo{left:534px;top:1068px}
.footer-logo .name{font-size:11px}
.copy{left:0;top:1175px;width:699px;text-align:center;font-size:5.5px;letter-spacing:.4px;color:#555}
</style>
</head>
<body>
<div class="page"></div>

<header>
  <div class="abs brand-row">
    <span class="brand-name">Gallant Stamper</span>
    <span class="brand-name">ZVN Rampart</span>
    <span class="brand-name">Gleaming Impressions</span>
    <span class="brand-name">Psalter Impressions</span>
    <span class="brand-name">RM Shimmer</span>
  </div>
  <div class="abs account"><span>MY ACCOUNT</span><span>-</span><span>MY CART</span><span>-</span><span>LOGIN</span><span>-</span><span>REGISTER</span></div>
  <div class="abs logo header-logo"><span class="dot"></span><span class="name">Press Upon Ink</span></div>
  <div class="abs call">
    <svg width="7" height="7" viewBox="0 0 10 10" style="vertical-align:-1px"><path d="M2 0.5 L4 2.5 L3 4 Q4.5 6 6 7 L7.5 6 L9.5 8 L8 9.5 Q3 9 0.5 2 Z" fill="#981e1e"/></svg>
    CALL US : <b>555-014-2290</b>
  </div>
  <div class="abs cart">
    <svg width="12" height="13" viewBox="0 0 12 13"><rect x="1" y="4" width="10" height="8.5" fill="none" stroke="#999"/><path d="M4 4 V2.5 a2 2 0 0 1 4 0 V4" fill="none" stroke="#999"/></svg>
    YOUR CART IS : 0 ITEMS
  </div>
  <div class="abs rule" style="left:58px;top:148px;width:584px"></div>
  <div class="abs rule" style="left:58px;top:150px;width:584px"></div>
  <nav class="abs nav">
    <span>HOME</span><span>SHOP</span><span>VIDEOS</span><span>GALLERY</span><span>BLOGS</span><span>SHOW SCHEDULE</span><span>PUI BRANDS</span><span>CONTACT US</span>
  </nav>
</header>

<section class="abs hero">
  <div class="hero-art" role="img" aria-label="Illustration of hanging shopping baskets, gift boxes, price tags and clouds"></div>
  <div class="offer">Special Offer</div>
  <div class="sale">SUPER<br>SALE</div>
  <div class="badge">50<small>%off</small></div>
  <div class="welcome">Welcome to<br><span class="brandline">PressUponInk,</span></div>
  <div class="tagline">Art Rubber Stamps and Scrapbooking<br>Supplies</div>
  <div class="btn">VIEW ALL PRODUCTS</div>
  <div class="arrows">
    <div><svg width="14" height="14"><path d="M8.5 4 L5.5 7 L8.5 10" fill="none" stroke="#fff"/></svg></div>
    <div><svg width="14" height="14"><path d="M5.5 4 L8.5 7 L5.5 10" fill="none" stroke="#fff"/></svg></div>
  </div>
</section>

<section>
  <div class="abs search-label">SEARCH YOUR FAVORITE PRODUCT</div>
  <div class="abs field" style="left:182px;top:480px;width:154px">AUTO SEARCH
    <svg width="8" height="8"><circle cx="3.3" cy="3.3" r="2.6" fill="none" stroke="#bbb"/><path d="M5.2 5.2 L7.5 7.5" stroke="#bbb"/></svg></div>
  <div class="abs field" style="left:342px;top:480px;width:106px">PRODUCTS <svg width="7" height="4"><path d="M0 0 H7 L3.5 4Z" fill="#888"/></svg></div>
  <div class="abs field" style="left:454px;top:480px;width:106px">PUI BRANDS <svg width="7" height="4"><path d="M0 0 H7 L3.5 4Z" fill="#888"/></svg></div>
  <div class="abs btn" style="left:566px;top:480px;width:76px;height:18px">SEARCH NOW</div>
  <div class="abs rule" style="left:58px;top:512px;width:584px"></div>
  <div class="abs featured">FEATURED PRODUCTS <small>ART RUBBER STAMPS AND SCRAPBOOKING SUPPLIES</small></div>
  <div class="abs rule" style="left:58px;top:543px;width:584px"></div>
  <div class="abs rule" style="left:58px;top:545px;width:584px"></div>
</section>

<main>
  <div class="abs card" style="left:58px;top:563px"><div class="shot" role="img" aria-label="Bottle of clear dimensional glaze on a pink card" style="background:linear-gradient(#f2b8c8,#f7dbe3)"></div><div class="title">EMBOSSING POWDER<br>AST. SPR</div><div class="price">$16.95</div><div class="btn">BUY NOW</div></div>
  <div class="abs card" style="left:207px;top:563px"><div class="shot" role="img" aria-label="Packaged embossing folder with lace border" style="background:linear-gradient(#cfe0ea,#b9d3e0)"></div><div class="title">EMBOSSING POWDER<br>AST. SPR</div><div class="price">$16.95</div><div class="btn">BUY NOW</div></div>
  <div class="abs card" style="left:357px;top:563px"><div class="shot" role="img" aria-label="Silver butterfly cutting die" style="background:linear-gradient(#eeeeee,#d8d8d8)"></div><div class="title">EMBOSSING POWDER<br>AST. SPR</div><div class="price">$16.95</div><div class="btn">BUY NOW</div></div>
  <div class="abs card" style="left:506px;top:563px"><div class="shot" role="img" aria-label="Silver lace border cutting die" style="background:linear-gradient(#ececec,#d6d6d6)"></div><div class="title">EMBOSSING POWDER<br>AST. SPR</div><div class="price">$16.95</div><div class="btn">BUY NOW</div></div>

  <div class="abs card" style="left:58px;top:759px"><div class="shot" role="img" aria-label="Swatches of glitter embossing powder in purple, blue, teal and sand" style="background:linear-gradient(135deg,#6b4a9c,#4d86b0,#3d8477,#d9c7a8)"></div><div class="title">EMBOSSING POWDER<br>AST. SPR</div><div class="price">$16.95</div><div class="btn">BUY NOW</div></div>
  <div class="abs card" style="left:207px;top:759px"><div class="shot" role="img" aria-label="Four painted cactus stamp cards" style="background:linear-gradient(135deg,#d9e4c8,#b6cf9c,#e8c7b8)"></div><div class="title">EMBOSSING POWDER<br>AST. SPR</div><div class="price">$16.95</div><div class="btn">BUY NOW</div></div>
  <div class="abs card" style="left:357px;top:759px"><div class="shot" role="img" aria-label="Sheet of black and white sticker outlines on red backing" style="background:linear-gradient(#c8323a,#e8e0e0 20%,#c9c9c9 80%,#c8323a)"></div><div class="title">EMBOSSING POWDER<br>AST. SPR</div><div class="price">$16.95</div><div class="btn">BUY NOW</div></div>
  <div class="abs card" style="left:506px;top:759px"><div class="shot" role="img" aria-label="Sheet of heart outline stickers on red backing" style="background:linear-gradient(#c8323a,#e8e0e0 20%,#c9c9c9 80%,#c8323a)"></div><div class="title">EMBOSSING POWDER<br>AST. SPR</div><div class="price">$16.95</div><div class="btn">BUY NOW</div></div>
</main>

<section>
  <div class="abs news-label">GET OUR RECENT UPDATES THROUGH YOUR EMAIL ID</div>
  <div class="abs field" style="left:258px;top:978px;width:169px">ENTER YOUR EMAIL ID :</div>
  <div class="abs btn" style="left:434px;top:978px;width:86px;height:18px">SUBSCRIBE</div>
  <div class="abs social"><div style="background:#3b5b9b"></div><div style="background:#1c7bb0"></div><div style="background:#e59a2a"></div><div style="background:#3aa7df"></div><div style="background:#c9221e"></div></div>
  <div class="abs rule" style="left:58px;top:1009px;width:584px"></div>
  <div class="abs rule" style="left:58px;top:1011px;width:584px"></div>
</section>

<footer>
  <div class="abs foot-col" style="left:58px"><h4>PRODUCTS</h4>ADHESIVES<br>ACCESSORIES<br>OUTLINE STICKERS(BY LUMO)<br>EDGE-MATS<br>RM SHIMMER PRODUCTS<br>ART ACETATES<br>GALLANT STAMPER STAMP LINE<br>DBL. EMBOSSED STICKERS</div>
  <div class="abs foot-col" style="left:202px"><h4>PUI BRANDS</h4>GALLANT STAMPER<br>ZVN RAMPART<br>GLEAMING IMPRESSIONS<br>PSALTER IMPRESSIONS<br>BRAVADO! STAMPS</div>
  <div class="abs foot-col" style="left:327px"><h4>CUSTOMER CARE</h4>CONTACT US<br>SIZE CHART<br>SHIPPING<br>INTERNATIONAL<br>RETURNS<br>FAQ<br>PRIVACY POLICY</div>
  <div class="abs foot-col" style="left:442px"><h4>INFORMATION</h4>TERMS &amp; CONDITIONS<br>PRIVACY POLICY<br>DISCLAIMER<br>SITEMAP</div>
  <div class="abs logo footer-logo"><span class="dot"></span><span class="name">Press Upon Ink</span></div>
  <div class="abs rule" style="left:58px;top:1162px;width:584px"></div>
  <div class="abs copy">COPYRIGHT © 2016. PRESS UPON INK. ALL RIGHTS RESERVED.</div>
</footer>
</body>
</html>
```